We need an eye catching logo design and Business Card that portrays our business, which is the cleaning and protecting of stainless steel with an organic non chemical product. This can be separate to the company name or can incorporate it. Maybe even just the company name itself. Company Name is Gleamwise Gleamwise.
Ideal for products exposed to weather elements, ie: balustrading, enclosures, BBQs, we also supply the product so you can do it yourself (DIY).
In addition we would want to include on this card:
1. My Name (Paul Dremmick)
2. Mobile No. (TBA Later)
3. Email address (TBA Later)
4. Web address (TBA Later)
Updates

Please note that we also need suggestions on a logo, as this we do not have this either.

Please note we have update our brief to be more specific.

Thank You.

Paul

Reason: Awaiting for a couple of revised submissions from feedback given.

Target Market(s)

Purchasing officers and government people.

Industry/Entity Type

Steel

Colors

Designer to choose colors to be used in the design.

Requirements
Must have
• 1. Name (Paul Dremmick)
2. Mobile No. (TBA Later)
Should not have
• Should not be to busy looking

```html
<!DOCTYPE html>
<html lang="en">
<head>
<meta charset="UTF-8">
<title>Gleamwise Gleamwise – Business Card</title>
<link rel="stylesheet" href="https://fonts.googleapis.com/css2?family=Anton&family=Source+Sans+3:wght@600;700&display=swap">
<style>
  :root {
    --page-bg: #e9e7e4;
    --card-dark: #141414;
    --card-silver: #b9bcbe;
    --silver-text: #c9cbcc;
    --ink: #1b1b1b;
    --website-text: #f2f2f2;
    --band-light: #f4f4f4;
    --band-dark: #4a4a4a;
    --dot-back: #8d9092;
  }
  * { margin: 0; padding: 0; box-sizing: border-box; }
  html, body { width: 1200px; height: 1000px; overflow: hidden; }
  body {
    background: var(--page-bg);
    font-family: "Source Sans 3", Arial, sans-serif;
    position: relative;
  }
  .card {
    position: absolute;
    left: 210px;
    width: 780px;
    height: 440px;
    border-radius: 34px;
    overflow: hidden;
    box-shadow: 0 10px 26px rgba(0,0,0,0.25);
  }
  .card--front {
    top: 45px;
    background:
      repeating-linear-gradient(180deg, transparent 0 2px, rgba(255,255,255,0.035) 2px 3px, transparent 3px 6px),
      linear-gradient(160deg, #2b2b2b 0%, var(--card-dark) 45%, #0c0c0c 100%);
  }
  .card--back {
    top: 515px;
    background:
      repeating-linear-gradient(180deg, transparent 0 2px, rgba(255,255,255,0.18) 2px 3px, transparent 3px 5px),
      linear-gradient(160deg, #d2d5d6 0%, var(--card-silver) 50%, #a7abad 100%);
  }
  .brand {
    position: absolute;
    display: flex;
    align-items: center;
  }
  .brand__dot {
    border-radius: 50%;
    flex: none;
  }
  .brand__name {
    font-family: "Anton", Impact, sans-serif;
    font-weight: 400;
    white-space: nowrap;
  }
  .card--front .brand { left: 90px; top: 140px; gap: 20px; }
  .card--front .brand__dot { width: 80px; height: 80px; background: var(--silver-text); }
  .card--front .brand__name { font-size: 54px; color: var(--silver-text); letter-spacing: 0.5px; }

  .band {
    position: absolute;
    height: 12px;
    background: linear-gradient(90deg, var(--band-dark), var(--band-light) 50%, var(--band-dark));
  }
  .card--front .band--left { left: 0; width: 330px; top: 352px; }
  .card--front .band--right { right: 0; width: 90px; top: 352px; }
  .website {
    position: absolute;
    left: 345px;
    top: 340px;
    font-size: 24px;
    line-height: 34px;
    font-weight: 600;
    color: var(--website-text);
    white-space: nowrap;
  }

  .card--back .brand__dot {
    position: absolute;
    left: 70px; top: 50px;
    width: 64px; height: 64px;
    background: var(--dot-back);
  }
  .card--back .brand__name {
    position: absolute;
    left: 62px; top: 150px;
    font-size: 40px;
    color: var(--ink);
  }
  .card--back .band { left: 0; right: 0; top: 222px; }
  .contact {
    position: absolute;
    right: 70px;
    bottom: 42px;
    text-align: right;
    color: var(--ink);
    font-weight: 700;
  }
  .contact__name { font-size: 38px; margin-bottom: 16px; }
  .contact__line { font-size: 24px; line-height: 1.2; }
</style>
</head>
<body>
  <section class="card card--front" aria-label="Business card front">
    <div class="brand">
      <span class="brand__dot"></span>
      <span class="brand__name">Gleamwise Gleamwise</span>
    </div>
    <span class="band band--left"></span>
    <span class="band band--right"></span>
    <p class="website">www.gleamwisegleamwise.com</p>
  </section>

  <section class="card card--back" aria-label="Business card back">
    <span class="brand__dot"></span>
    <span class="brand__name">Gleamwise Gleamwise</span>
    <span class="band"></span>
    <div class="contact">
      <p class="contact__name">Paul Dremmick</p>
      <p class="contact__line">0400 718 265</p>
      <p class="contact__line">youremail@mailbox.com</p>
    </div>
  </section>
</body>
</html>
```